KRTLO Promotion Flyer to raise money and communicate our goals

We need a flyer that promotes our organization. We are a 501(c)3 trying to raise money for Arts, Education and Entrepreneurship in our small town.

We promote a social events that improve qualtiy of life and educate people on how to start and expand businesses. Our goal is to make downtown an active and thriving place with many things for people to do and enjoy as well as create a favorable place for business.

Target Market(s)

Wealthy donors and Organizations with cash

Industry/Entity Type

Education

Colors

Designer to choose colors to be used in the design.

Requirements
Must have
• Eye catching graphics and look very professional
• Should appeal to men and women
Nice to have
• Make use of any known psychological colors and fonts etc... that appeal to philanthropic people
Should not have
• Should not be complicated or confusing

```html
<!DOCTYPE html>
<html lang="en">
<head>
<meta charset="utf-8">
<title>KRTLO – Arts, Education and Entrepreneurship</title>
<link rel="stylesheet" href="https://fonts.googleapis.com/css2?family=Alfa+Slab+One&family=Marcellus&family=Cabin:wght@400;600&family=Lato:wght@300&family=Lora:ital,wght@1,500&display=swap">
<style>
  :root{
    --ink-black:#0d0d0d;
    --paper:#ffffff;
    --title-red:#e0141d;
    --band-red:#e31b23;
    --slate:#555a5f;
    --sky-blue:#29a8df;
    --deep-blue:#1673c2;
    --column-blue:#4bb6e6;
    --text-grey:#4a4a4a;
  }
  *{margin:0;padding:0;box-sizing:border-box}
  html,body{width:942px;height:1200px;overflow:hidden;background:var(--ink-black)}
  .flyer{position:absolute;left:28px;top:28px;width:886px;height:1144px;background:var(--paper);overflow:hidden}
  .headline{position:absolute;left:42px;top:42px;width:640px}
  .headline-main{font-family:"Alfa Slab One",serif;color:var(--title-red);font-size:46px;line-height:58px;transform:scaleX(.9);transform-origin:left top;white-space:nowrap}
  .headline-sub{font-family:"Marcellus",serif;color:var(--slate);font-size:41px;letter-spacing:1px;margin-top:-2px}
  .brand{position:absolute;left:588px;top:64px;width:250px;text-align:center}
  .brand-name{font-family:"Cabin",sans-serif;font-weight:600;font-size:44px;color:var(--deep-blue);display:flex;align-items:center;justify-content:center;gap:10px}
  .brand-name .mark{width:22px;height:22px;background:var(--deep-blue)}
  .brand-tag{font-family:"Cabin",sans-serif;font-weight:600;font-size:15px;color:var(--deep-blue);margin-top:6px;line-height:19px}
  .hero{position:absolute;left:0;top:0}
  .inset{position:absolute;left:32px;top:484px;width:160px;height:244px}
  .intro{position:absolute;left:200px;top:656px;width:652px;text-align:right;font-family:"Lato",sans-serif;font-weight:300;font-size:19px;line-height:27px;color:var(--text-grey);white-space:nowrap}
  .membership{position:absolute;left:22px;top:750px;width:840px;height:204px;background:var(--sky-blue)}
  .membership-lead{position:absolute;left:18px;top:6px;width:510px;font-family:"Cabin",sans-serif;font-weight:600;font-size:14px;line-height:22px;color:var(--paper)}
  .pillar{position:absolute;top:56px;height:148px;background:var(--column-blue);color:var(--paper);font-family:"Cabin",sans-serif;font-size:13.4px;line-height:16.6px;text-align:center;padding:4px 6px}
  .pillar strong{display:block;font-weight:400;margin-bottom:4px}
  .forest{position:absolute;left:540px;top:6px;width:294px;height:192px}
  .appeal{position:absolute;left:23px;top:968px;width:839px;font-family:"Cabin",sans-serif;font-size:12.6px;line-height:20px;color:var(--text-grey)}
  .appeal span{display:block;white-space:nowrap}
  .appeal .full{text-align:justify;text-align-last:justify}
  .appeal .close{text-align:center}
  .footer{position:absolute;left:0;bottom:0}
  .web{position:absolute;left:32px;top:1094px;font-family:"Lora",serif;font-style:italic;font-weight:500;font-size:27px;letter-spacing:1px;color:var(--paper)}
</style>
</head>
<body>
<main class="flyer">
  <svg class="hero" width="886" height="660" viewBox="0 0 886 660">
    <defs>
      <linearGradient id="parkTones" x1="0" y1="0" x2="0" y2="1">
        <stop offset="0" stop-color="#ffffff"/>
        <stop offset=".12" stop-color="#dfe6ea"/>
        <stop offset=".35" stop-color="#b9b5a8"/>
        <stop offset=".5" stop-color="#6f8f48"/>
        <stop offset="1" stop-color="#86ad4f"/>
      </linearGradient>
    </defs>
    <path d="M0 580 C240 652 560 648 886 596 L886 630 C560 668 300 664 200 640 Z" fill="var(--deep-blue)"/>
    <path role="img" aria-label="Photo of the town park with lawn, young trees, gazebo and community hall" d="M0 212 L886 212 L886 590 C560 640 260 650 0 530 Z" fill="url(#parkTones)"/>
  </svg>

  <header class="headline">
    <h1 class="headline-main">ARTS, EDUCATION AND<br>ENTREPRENEURSHIP</h1>
    <p class="headline-sub">IN OUR SMALL TOWN</p>
  </header>

  <div class="brand">
    <div class="brand-name"><span class="mark"></span>KRTLO</div>
    <div class="brand-tag">Cedar Hollow<br>Small Business Association</div>
  </div>

  <svg class="inset" viewBox="0 0 160 244">
    <path d="M6 10 Q6 2 14 2 L136 2 L158 -14 L152 12 L152 236 Q152 242 146 242 L12 242 Q6 242 6 236 Z" fill="var(--band-red)"/>
    <rect role="img" aria-label="Photo of the town welcome sign at the park entrance" x="14" y="10" width="130" height="224" rx="6" fill="#9fb0a0"/>
  </svg>

  <p class="intro">The Cedar Hollow Small Business Association (KRTLO) is a local leader<br>in the areas of Arts, Education and Entrepreneurship and is working<br>diligently to promote Cedar Hollow and revitalize our downtown.</p>

  <section class="membership">
    <p class="membership-lead">When you become an KRTLO Member, you will be a part of the citywide work that the KRTLO does every day to improve the lives of citizens of Cedar Hollow:</p>
    <div class="pillar" style="left:18px;width:131px"><strong>We promote</strong>Cedar Hollow Hotels, Shopping and Events that make Cedar Hollow a pleasant, exciting and prosperous place to live.</div>
    <div class="pillar" style="left:156px;width:118px"><strong>We provide</strong>training and resources to anyone interested Arts, Education and Entrepreneurship.</div>
    <div class="pillar" style="left:282px;width:116px"><strong>We help</strong>entrepreneur's start and grow their businesses in a tax efficient and appropriate way.</div>
    <div class="pillar" style="left:406px;width:124px"><strong>We work</strong>with all levels of local government to promote our community and create a fertile environment for growth.</div>
    <svg class="forest" viewBox="0 0 294 192" role="img" aria-label="Photo of a sunlit pine forest">
      <defs>
        <linearGradient id="forestTones" x1="0" y1="0" x2="0" y2="1">
          <stop offset="0" stop-color="#5c5a4c"/>
          <stop offset=".45" stop-color="#c9c2a0"/>
          <stop offset="1" stop-color="#4d6a26"/>
        </linearGradient>
      </defs>
      <rect width="294" height="192" fill="url(#forestTones)"/>
    </svg>
  </section>

  <p class="appeal">
    <span class="full">Every day, we look for ways to help our local businesses grow and expand, but we need you by our side. As an KRTLO Member, you can help</span>
    <span class="full">provide training, education and support, and you can give our many businesses a chance to grow and our citizens the opportunity to</span>
    <span class="full">experience big town amenities and events in a small town. Members' regular monthly gifts provide a consistent, reliable income stream that</span>
    <span class="full">allows us to spend less time fundraising—and more time helping our businesses and community. Becoming an KRTLO Member is an easy,</span>
    <span class="close">efficient and tax-deductible way to make a difference for our community all year</span>
    <span class="close">long. Please donate today.</span>
  </p>

  <svg class="footer" width="886" height="110" viewBox="0 0 886 110">
    <path d="M0 58 C260 46 560 74 886 62 L886 110 L0 110 Z" fill="var(--band-red)"/>
    <path d="M220 42 C420 64 680 66 886 14 L886 62 C660 98 420 72 220 42 Z" fill="var(--deep-blue)"/>
  </svg>
  <p class="web">www.CedarArtsFund.org</p>
</main>
</body>
</html>
```